We need a wordpress design that will incorporate a professional color scheme with company logo in a clean layout. The design needs to consider that this will be developed on a responsive theme. Colors are blue and green of the logo and and an accent color (perhaps very light brown/tan). Client wants a 'modern' look.

Industry/Entity Type

It Company

Font styles to use
Serif
Sans Serif

Colors

Designer to choose colors to be used in the design.

Requirements
Must have
• navigation: 1) Home; 2) Services; 3) Auctions by Type; 4) About Us; 5) KVL Digest 6) Videos; 7) Contact Us

VERY general idea of layout is attached, Site will have slideshow, image is attached. Widgets used to are: 1) Email Contact Form; 2) social media icons, FB LinedIn, YouTube; 3) Featured Auctions; 4) News & Events blog; Featured Video

Footer will have affiliation logos, contact info and perhaps smaller company logo:
Phone: (512) 555-0147 / Mobile: (512) 555-0193 (Denise)
Email: dpettiford482@mailbright.net / wade@harlowpettiford.com
Address: 417 Quarry Bend Rd • #B214 • PMB715 • Austin, TX 78799

Nice to have
• Use of a dropdown menu

```html
<!DOCTYPE html>
<html lang="en">
<head>
<meta charset="utf-8">
<title>Harlow Pettiford Auction Marketing</title>
<link href="https://fonts.googleapis.com/css2?family=Lato:wght@400;700&family=Roboto:wght@400;500;700&display=swap" rel="stylesheet">
<style>
:root{
  --blue:#175a9f;
  --blue-dark:#0e4d94;
  --link:#1b63ad;
  --text:#333;
  --muted:#777;
  --panel:#f5f5f5;
  --line:#e3e3e3;
  --star:#f0a81c;
}
*{box-sizing:border-box;margin:0;padding:0}
html,body{width:676px;height:1200px;overflow:hidden;background:#fff}
body{position:relative;font-family:'Lato',sans-serif;color:var(--text)}
.abs{position:absolute}
.brand{left:98px;top:16px;width:110px;text-align:center;color:var(--blue);font-weight:700;line-height:1.05}
.brand .top{font-size:15px}
.brand .bottom{font-size:10px;margin-top:4px}
.contact-top{left:344px;top:28px}
.contact-top svg{position:absolute;left:0;top:4px}
.contact-top .phone{margin-left:32px;font-family:'Roboto',sans-serif;font-weight:500;font-size:9px;color:var(--blue)}
.contact-top .mail{margin-left:32px;margin-top:4px;font-size:8.5px;color:#666}
.social-top{left:529px;top:37px;display:flex;gap:4px}
.social-top span{width:15px;height:15px;border-radius:50%;display:block}
.hero{left:0;top:102px;width:676px;height:311px;background:linear-gradient(160deg,#6f8a7b 0%,#4e6e60 35%,#5d6b66 60%,#8b8f88 100%)}
.arrow{width:19px;height:19px;border-radius:50%;background:#222;display:flex;align-items:center;justify-content:center;top:251px}
.nav{left:97px;top:86px;width:483px;height:31px;background:var(--blue);display:flex;align-items:center;padding-left:11px}
.nav a{color:#fff;text-decoration:none;font-size:9.5px;margin-right:29px;display:flex;align-items:center;gap:6px}
.dropdown{left:153px;top:120px;width:137px;height:91px;background:#fff;box-shadow:0 1px 4px rgba(0,0,0,.2);padding:6px 10px}
.dropdown::before{content:"";position:absolute;left:7px;top:-5px;border:5px solid transparent;border-top:0;border-bottom-color:#fff}
.dropdown div{font-size:7.2px;color:#555;height:20.3px;line-height:20.3px;border-bottom:1px solid #eee}
.dropdown div:last-child{border-bottom:0}
.services{left:97px;top:356px;width:483px;height:130px;background:#fff;border:1px solid var(--line);box-shadow:0 6px 8px -6px rgba(0,0,0,.25);display:flex;padding-top:12px}
.service{flex:1;text-align:center}
.service svg{display:block;margin:0 auto}
.service .shadow{width:46px;height:3px;margin:4px auto 9px;background:radial-gradient(ellipse,rgba(0,0,0,.18),transparent 70%)}
.service h3{font-weight:400;font-size:9px;color:var(--link);margin-bottom:6px}
.service p{font-size:6.4px;color:#777;line-height:1.6}
.section-title{font-size:10px;color:#333;font-weight:400;text-transform:uppercase}
.upcoming{top:536px;width:240px;height:94px}
.thumb{position:absolute}
.upcoming .thumb{left:0;top:0;width:100px;height:93px}
.upcoming .body{position:absolute;left:112px;top:0;width:128px}
.upcoming h4{font-weight:400;font-size:8.8px;color:#333}
.upcoming .sub{font-size:7.2px;color:var(--link);margin-top:5px}
.upcoming p{font-size:6.4px;color:#666;line-height:1.8;margin-top:6px}
.upcoming .more{font-size:6.2px;color:#555;margin-top:6px}
.featured-band{left:0;top:653px;width:676px;height:189px;background:var(--panel);border-top:1px solid #ececec}
.card{top:691px;width:152px;height:131px;background:#fff;border:1px solid #e8e8e8}
.card .thumb{left:0;top:0;width:150px;height:88px}
.card h4{position:absolute;left:8px;top:97px;font-weight:400;font-size:8.6px;color:#333}
.card .loc{position:absolute;left:6px;top:114px;font-size:7.4px;color:var(--link)}
.video{left:97px;top:888px;width:199px;height:147px;background:#2b2b2b;padding:4px}
.video .screen{width:191px;height:130px;background:linear-gradient(180deg,#6f9fd6 0%,#bcd6ee 55%,#d9c9a9 100%)}
.video .play{position:absolute;left:79px;top:51px;width:36px;height:36px;border-radius:50%;background:rgba(60,60,60,.75)}
.video .bar{position:absolute;left:4px;bottom:2px;width:191px;height:11px;display:flex;align-items:center;gap:7px;padding-left:6px;font-size:5px;color:#bbb}
.post{left:315px;width:266px;height:67px}
.post .thumb{left:0;top:0;width:83px;height:66px}
.post .body{position:absolute;left:98px;top:0;width:168px}
.post h4{font-weight:400;font-size:7.3px;color:#333;letter-spacing:.2px}
.post .rating{font-size:7px;margin-top:5px;color:#555}
.post .rating b{color:var(--star);font-weight:400;margin-right:9px}
.post .rating i{color:#ccc;font-style:normal}
.post p{font-size:5.9px;color:#777;line-height:1.8;margin-top:5px}
.post .more{font-size:5.6px;color:#333;margin-top:7px}
.footer{left:0;top:1062px;width:676px;height:106px;background:#f3f3f3}
.footer h5{position:absolute;left:97px;top:17px;font-weight:400;font-size:9.5px;color:var(--link)}
.footer .row{position:absolute;left:97px;font-size:6.4px;color:#444;display:flex;align-items:center}
.footer .row svg{margin-right:11px}
.mini-brand{position:absolute;left:300px;top:42px;width:60px;text-align:center;color:var(--blue);font-weight:700;font-size:7px;line-height:1.15}
.badges{position:absolute;left:387px;top:40px;width:54px;display:grid;grid-template-columns:repeat(2,22px);gap:4px 6px}
.badges span{display:block;height:14px;background:#555}
.badges span.round{border-radius:50%;width:14px}
.newsletter{left:461px;top:1062px;width:120px;height:106px;background:var(--blue-dark);padding:10px 16px}
.newsletter h6{font-weight:400;font-size:8px;color:#fff;letter-spacing:.3px}
.newsletter .field{background:#fff;height:15px;margin-top:7px;font-size:5.3px;color:#666;padding:4px 6px}
.newsletter .field:first-of-type{margin-top:10px}
.newsletter .btn{margin-top:9px;display:inline-block;border:1px solid #fff;border-radius:3px;color:#fff;font-size:6.2px;padding:3px 6px}
.bottom-bar{left:0;top:1168px;width:676px;height:32px;background:var(--blue-dark);color:#fff;font-size:6.2px}
.bottom-bar .copy{position:absolute;left:97px;top:12px}
.bottom-bar .icons{position:absolute;left:525px;top:8px;display:flex;gap:5px}
.bottom-bar .icons span{width:15px;height:15px;border:1px solid #fff;border-radius:50%;display:block}
</style>
</head>
<body>

<div class="abs brand">
  <div class="top">Prairie Crest</div>
  <div class="bottom">Harlow Pettiford<br>Auction Marketing</div>
</div>

<div class="abs contact-top">
  <svg width="20" height="22" viewBox="0 0 20 22"><path d="M5 2c1 0 3 3 3 4s-2 2-2 3 3 6 5 7c1 0 2-2 3-2s4 2 4 3-2 3-4 3C8 20 2 12 2 6c0-2 2-4 3-4z" fill="#e9e9e9"/></svg>
  <div class="phone">Austin Office: 512-555-0147</div>
  <div class="mail">info@harlowpettiford.com</div>
</div>

<div class="abs social-top">
  <span style="background:#3b5b9a"></span>
  <span style="background:#2aa6de"></span>
  <span style="background:#d0302a"></span>
</div>

<div class="abs hero" role="img" aria-label="Slideshow photo of an industrial machine shop floor with green lathes"></div>
<div class="abs arrow" style="left:29px"><svg width="8" height="8" viewBox="0 0 8 8"><path d="M5.5 1L2.5 4l3 3" stroke="#fff" stroke-width="1.5" fill="none"/></svg></div>
<div class="abs arrow" style="left:624px"><svg width="8" height="8" viewBox="0 0 8 8"><path d="M2.5 1l3 3-3 3" stroke="#fff" stroke-width="1.5" fill="none"/></svg></div>

<nav class="abs nav">
  <a href="#">Home</a>
  <a href="#">Services <svg width="6" height="4" viewBox="0 0 6 4"><path d="M.5.5 3 3 5.5.5" stroke="#fff" fill="none"/></svg></a>
  <a href="#">Auctions by Type</a>
  <a href="#">About Us</a>
  <a href="#">KVL Digest</a>
  <a href="#">Videos</a>
  <a href="#">Contact</a>
</nav>

<div class="abs dropdown">
  <div>Real Estate Auctions</div>
  <div>Business Liquidations</div>
  <div>Commercial &amp; Industrial Auctions</div>
  <div>Appraisal Services</div>
</div>

<section class="abs services">
  <div class="service">
    <svg width="44" height="40" viewBox="0 0 44 40"><path d="M22 4 8 16h4v10h20V16h4z" fill="none" stroke="#1b5fa6" stroke-width="3"/><rect x="19" y="17" width="6" height="9" fill="#1b5fa6"/><path d="M2 22c4 0 8 10 14 14h12c6-4 10-14 14-14" fill="none" stroke="#1b5fa6" stroke-width="3"/></svg>
    <div class="shadow"></div>
    <h3>Real Estate Auctions</h3>
    <p>Lorem ipsum dolor sit amet,<br>consectetur adipiscing elit,</p>
  </div>
  <div class="service">
    <svg width="44" height="40" viewBox="0 0 44 40"><rect x="16" y="2" width="18" height="36" fill="#1b5fa6"/><rect x="6" y="14" width="12" height="24" fill="#2f74bb"/><g fill="#fff"><rect x="19" y="6" width="3" height="3"/><rect x="25" y="6" width="3" height="3"/><rect x="19" y="13" width="3" height="3"/><rect x="25" y="13" width="3" height="3"/><rect x="19" y="20" width="3" height="3"/><rect x="25" y="20" width="3" height="3"/><rect x="9" y="18" width="3" height="3"/><rect x="9" y="25" width="3" height="3"/></g></svg>
    <div class="shadow"></div>
    <h3>Commercial &amp; Industrial</h3>
    <p>Lorem ipsum dolor sit amet,<br>consectetur adipiscing elit,</p>
  </div>
  <div class="service">
    <svg width="44" height="40" viewBox="0 0 44 40"><rect x="6" y="4" width="32" height="22" rx="4" fill="none" stroke="#1b5fa6" stroke-width="3"/><circle cx="17" cy="20" r="5" fill="#1b5fa6"/><circle cx="27" cy="20" r="5" fill="#1b5fa6"/><path d="M10 38c0-8 4-11 7-11s7 3 7 11zM20 38c0-8 4-11 7-11s7 3 7 11z" fill="#1b5fa6"/></svg>
    <div class="shadow"></div>
    <h3>Business Liquidations</h3>
    <p>Lorem ipsum dolor sit amet,<br>consectetur adipiscing elit,</p>
  </div>
  <div class="service">
    <svg width="44" height="40" viewBox="0 0 44 40"><path d="M22 3 36 9v20l-14 8-14-8V9z" fill="none" stroke="#1b5fa6" stroke-width="3"/><path d="M8 9l14 7 14-7M22 16v21" stroke="#1b5fa6" stroke-width="3" fill="none"/><path d="M22 16 36 9v20l-14 8z" fill="#1b5fa6"/></svg>
    <div class="shadow"></div>
    <h3>Appraisal Services</h3>
    <p>Lorem ipsum dolor sit amet,<br>consectetur adipiscing elit,</p>
  </div>
</section>

<h2 class="abs section-title" style="left:97px;top:508px">Upcoming Auctions</h2>

<article class="abs upcoming" style="left:97px">
  <div class="thumb" role="img" aria-label="Aerial photo of an island neighbourhood on a lake" style="background:linear-gradient(180deg,#8fb8df 0%,#5c8fbf 45%,#6f7f6a 75%,#3f6f8f 100%)"></div>
  <div class="body">
    <h4>SEALED BID AUCTION</h4>
    <div class="sub">Sealed Bid Auction</div>
    <p>Cedar Point Isle opened in 1983 as America's most prestigious and secure residential lakefront address. It along with Sereno, Lago Sereno,</p>
    <div class="more">Read More +</div>
  </div>
</article>

<article class="abs upcoming" style="left:349px">
  <div class="thumb" role="img" aria-label="Photo of a wooded lot with a fence and trees" style="background:linear-gradient(180deg,#5f7f4c 0%,#7f9a62 50%,#9a9478 100%)"></div>
  <div class="body">
    <h4>SEALED BID AUCTION</h4>
    <div class="sub">Sealed Bid Auction</div>
    <p>Cedar Point Isle opened in 1983 as America's most prestigious and secure residential lakefront address. It along with Sereno, Lago Sereno,</p>
    <div class="more">Read More +</div>
  </div>
</article>

<div class="abs featured-band"></div>
<h2 class="abs section-title" style="left:97px;top:665px">Featured Auctions</h2>

<article class="abs card" style="left:97px">
  <div class="thumb" role="img" aria-label="Photo of a white single-storey house with a lawn" style="background:linear-gradient(180deg,#9cb58a 0%,#c9d2d3 45%,#6e8f4c 100%)"></div>
  <h4>22 Ready to Build On Lots</h4>
  <div class="loc">Location:&nbsp; Cedar Point Isle</div>
</article>
<article class="abs card" style="left:263px">
  <div class="thumb" role="img" aria-label="Photo of a two-storey suburban house" style="background:linear-gradient(180deg,#7fb2e6 0%,#d8c8a8 50%,#7c9a55 100%)"></div>
  <h4>22 Ready to Build On Lots</h4>
  <div class="loc">Location:&nbsp; Cedar Point Isle</div>
</article>
<article class="abs card" style="left:430px">
  <div class="thumb" role="img" aria-label="Photo of a house with a large garage and driveway" style="background:linear-gradient(180deg,#6f8f5a 0%,#c9b9a2 45%,#8f8a80 100%)"></div>
  <h4>22 Ready to Build On Lots</h4>
  <div class="loc">Location:&nbsp; Cedar Point Isle</div>
</article>

<h2 class="abs section-title" style="left:97px;top:864px">Featured Video</h2>
<h2 class="abs section-title" style="left:315px;top:864px">News &amp; Events Blog</h2>

<div class="abs video">
  <div class="screen" role="img" aria-label="Video still of a small model house and a hand holding keys against a cloudy sky"></div>
  <div class="play"><svg width="36" height="36" viewBox="0 0 36 36"><path d="M14 11l12 7-12 7z" fill="#fff"/></svg></div>
  <div class="bar">
    <svg width="5" height="6" viewBox="0 0 5 6"><path d="M0 0l5 3-5 3z" fill="#bbb"/></svg>
    <span>◂×</span><span>0:00 / 5:17</span>
  </div>
</div>

<article class="abs post" style="top:889px">
  <div class="thumb" role="img" aria-label="Photo of a couple receiving house keys outside a home" style="background:linear-gradient(180deg,#9fb9d6 0%,#a9a495 55%,#6f8f56 100%)"></div>
  <div class="body">
    <h4>VIVAMUS VESTIBULUM NULLA NEC ANTE</h4>
    <div class="rating"><b>★★★<i>☆☆</i></b>3967 reviews</div>
    <p>Sed egestas, ante et vulputate volutpat, eros pede semper vitae luctus metus libero eu augue. Morbi purus libero,</p>
    <div class="more">LEARN MORE</div>
  </div>
</article>

<article class="abs post" style="top:968px">
  <div class="thumb" role="img" aria-label="Photo of a family in front of their house" style="background:linear-gradient(180deg,#c7d6e4 0%,#a39a8d 50%,#6e9152 100%)"></div>
  <div class="body">
    <h4>VIVAMUS VESTIBULUM NULLA NEC ANTE</h4>
    <div class="rating"><b>★★★<i>☆☆</i></b>3967 reviews</div>
    <p>Sed egestas, ante et vulputate volutpat, eros pede semper vitae luctus metus libero eu augue. Morbi purus libero,</p>
    <div class="more">LEARN MORE</div>
  </div>
</article>

<footer class="abs footer">
  <h5>HARLOW PETTIFORD</h5>
  <div class="row" style="top:41px"><svg width="6" height="8" viewBox="0 0 6 8"><path d="M3 0a3 3 0 0 0-3 3c0 2 3 5 3 5s3-3 3-5a3 3 0 0 0-3-3z" fill="#1b63ad"/><circle cx="3" cy="3" r="1" fill="#f3f3f3"/></svg>417 Quarry Bend Rd, #B214, PMB 715 Austin, Texas 78799</div>
  <div class="row" style="top:61px"><svg width="7" height="7" viewBox="0 0 7 7"><path d="M1.5 0c.5 0 1.5 1.5 1.5 2S2 3 2.5 3.5 4 5 4.5 4.5 5 4 5.5 4s1.5 1 1.5 1.5S6 7 5 7C2.5 7 0 4.5 0 2 0 1 1 0 1.5 0z" fill="#1b63ad"/></svg>Phone: (512) 555-0147 / Mobile: (512) 555-0193 (Denise)</div>
  <div class="row" style="top:80px"><svg width="7" height="6" viewBox="0 0 7 6"><rect x=".5" y=".5" width="6" height="5" fill="none" stroke="#1b63ad"/><path d="M.5.5 3.5 3l3-2.5" stroke="#1b63ad" fill="none"/></svg>dpettiford482@mailbright.net / wade@harlowpettiford.com</div>
  <div class="mini-brand">Prairie Crest<br><span style="font-size:5.5px">Harlow Pettiford<br>Auction Marketing</span></div>
  <div class="badges">
    <span class="round"></span><span></span>
    <span></span><span></span>
  </div>
</footer>

<aside class="abs newsletter">
  <h6>NEWSLETTER</h6>
  <div class="field">Enter Your Name</div>
  <div class="field">Enter Your Email</div>
  <div class="btn">subscribe</div>
</aside>

<div class="abs bottom-bar">
  <div class="copy">© 2014 Harlow Pettiford Auction Marketing, Inc. - All Rights Reserved</div>
  <div class="icons"><span></span><span></span><span></span></div>
</div>

</body>
</html>
```